Larder & Flame - Premium Catering needs a new menu design.

I currently use menupro to make my own menus for printing and uploading to the website (PDF). I need a professional menu to replace my current menu. I wold like to mail these menus out so I'm thinking a tri-fold menu would be the best option. Similar to what pizzerias send out.

Logo Text

Would be good to reduce the text thickness of the letters "MIL" in the word MILLRUN. Right now MIL has thicker text.

Colors

Designer to choose colors to be used in the design.

```html
<!DOCTYPE html>
<html lang="en">
<head>
<meta charset="utf-8">
<title>Millrun Menu</title>
<link href="https://fonts.googleapis.com/css2?family=Fira+Sans+Condensed:wght@400;500;600&display=swap" rel="stylesheet">
<style>
:root{
  --backdrop:#555555;
  --paper:#ffffff;
  --gold:#b8932e;
  --wine:#8b1a1a;
  --ink:#222222;
  --dash-h:repeating-linear-gradient(90deg,var(--gold) 0 14px,transparent 14px 24px);
  --dash-v:repeating-linear-gradient(180deg,var(--gold) 0 14px,transparent 14px 24px);
}
*{box-sizing:border-box;margin:0;padding:0}
html,body{width:1200px;height:1200px;overflow:hidden;background:var(--backdrop)}
.stage{position:absolute;left:0;top:0;width:1932px;height:1932px;transform:scale(0.621118);transform-origin:0 0;font-family:"Fira Sans Condensed",sans-serif;color:var(--ink)}
.page{position:absolute;left:250px;top:40px;width:1432px;height:1852px;background:var(--paper)}
.frame{position:absolute;left:273px;top:63px;width:1386px;height:1805px;border:4px solid var(--gold)}
.divider{position:absolute;left:964px;top:207px;height:1603px;width:3px;background:var(--dash-v)}
.heading{position:absolute;text-align:center;color:var(--gold);font-weight:600;letter-spacing:2px}
.heading .title{display:inline-flex;align-items:center;gap:12px;line-height:1}
.heading .title::before,.heading .title::after{content:"";display:block;width:40px;height:7px;background:var(--gold)}
.heading .sub{font-size:19px;font-weight:500;letter-spacing:.5px;margin-top:8px;line-height:24px}
.t-xl{font-size:62px}
.t-l{font-size:46px}
.t-m{font-size:33px}
.wings-head{left:332px;width:590px;top:90px;font-size:36px;line-height:46px}
.wings-head .bar{position:absolute;top:36px;width:40px;height:7px;background:var(--gold)}
.menu-list{position:absolute;width:590px;list-style:none;padding-bottom:3px}
.menu-list::after{content:"";position:absolute;left:0;right:0;bottom:0;height:3px;background:var(--dash-h)}
.col-left{left:332px}
.col-right{left:1010px}
.item{position:relative;height:var(--h,101px);padding-top:9px}
.item::before{content:"";position:absolute;left:0;right:0;top:0;height:3px;background:var(--dash-h)}
.row{display:flex;align-items:center;height:40px}
.name{color:var(--wine);font-weight:500;font-size:32px;white-space:nowrap;display:flex;align-items:center;gap:6px}
.rule{flex:1;border-top:1.5px solid var(--gold);margin:0 10px;min-width:20px}
.price{color:var(--wine);font-weight:600;font-size:22px;letter-spacing:1px;width:62px;text-align:right}
.desc{font-size:18px;font-weight:500;line-height:23px;margin-top:4px}
.tag{display:inline-flex;flex-direction:column;align-items:center;font-size:11px;line-height:11px;font-weight:400;color:var(--wine)}
.wings-prices{margin-left:auto;display:grid;grid-template-columns:auto 40px auto;gap:2px 8px;align-items:center;font-size:20px;font-weight:600}
.wings-prices .qty{color:var(--gold)}
.wings-prices .dash{border-top:1.5px solid var(--gold)}
.wings-prices .amt{color:var(--wine);font-size:22px;text-align:right;width:76px}
.footer{position:absolute;left:795px;top:1826px;width:342px;height:32px;text-align:center;color:var(--gold);font-size:19px;font-weight:500;line-height:28px;border-bottom:3px solid var(--gold)}
.footer::before,.footer::after{content:"";position:absolute;bottom:-3px;width:3px;height:9px;background:var(--gold)}
.footer::before{left:0}
.footer::after{right:0}
</style>
</head>
<body>
<div class="stage">
  <div class="page"></div>
  <div class="frame"></div>
  <div class="divider"></div>

  <div class="heading wings-head">
    <span class="bar" style="left:6px"></span>
    <div>MILLRUN JUMBO WINGS</div>
    <div>&amp; CHICKEN FINGERS</div>
    <span class="bar" style="right:6px"></span>
  </div>
  <ul class="menu-list col-left" style="top:205px">
    <li class="item" style="--h:144px">
      <div class="row" style="height:70px;align-items:flex-start;padding-top:4px">
        <span class="name">Jumbo Wings</span>
        <div class="wings-prices">
          <span class="qty">6 Pieces</span><span class="dash"></span><span class="amt">$&nbsp;&nbsp; 7.99</span>
          <span class="qty">12 Pieces</span><span class="dash"></span><span class="amt">$ 12.99</span>
        </div>
      </div>
      <p class="desc">Buffalo, garlic buffalo, or honey BBQ. Choice of mild, medium, hot, or insane.<br>Buffalo wings are served with bleu cheese dressing and celery sticks.</p>
    </li>
    <li class="item"><div class="row"><span class="name">Chicken Fingers</span><span class="rule" style="margin-left:110px"></span><span class="price">$ 8.49</span></div><p class="desc">Served with fries and honey mustard.</p></li>
    <li class="item"><div class="row"><span class="name">Buffalo Chicken Fingers</span><span class="rule"></span><span class="price">$ 8.99</span></div><p class="desc">Served with fries and blue cheese.</p></li>
  </ul>

  <div class="heading" style="left:332px;width:590px;top:598px">
    <div class="title t-xl">WRAPS</div>
    <div class="sub">SERVED WITH COMPLEMENTARY FRENCH FRIES</div>
  </div>
  <ul class="menu-list col-left" style="top:741px">
    <li class="item"><div class="row"><span class="name">Chicken Caesar Wrap</span><span class="rule" style="margin-left:40px"></span><span class="price">$ 8.49</span></div><p class="desc">Grilled chicken breast with shredded lettuce, tomatoes, red onion, Romano cheese, and Caesar dressing.</p></li>
    <li class="item"><div class="row"><span class="name">Chicken &amp; Broccoli Wrap</span><span class="rule" style="margin-left:24px"></span><span class="price">$ 8.99</span></div><p class="desc">Grilled chicken, chopped broccoli, Romano cheese, and garlic topped with melted Colby sharp cheese.</p></li>
    <li class="item"><div class="row"><span class="name">Cowgirl Chicken Wrap</span><span class="rule" style="margin-left:30px"></span><span class="price">$ 8.99</span></div><p class="desc">Grilled chicken breast with Monterey Jack cheese, bacon, shredded lettuce, and honey mustard.</p></li>
    <li class="item"><div class="row"><span class="name">Crispy Chicken Buffalo Wrap <span class="tag"><svg width="30" height="16" viewBox="0 0 30 16"><path d="M3 13 C10 13 20 9 24 3 L27 5 C22 12 12 16 3 13Z" fill="#c8201e"/><path d="M24 3 L26 0" stroke="#3b7a2a" stroke-width="2"/></svg>spicy</span></span><span class="rule"></span><span class="price">$ 9.29</span></div><p class="desc">Chicken cutlet with buffalo sauce, shredded lettuce, tomato,<br>and ranch dressing.</p></li>
    <li class="item"><div class="row" style="margin-top:12px"><span class="name">Crispy Chicken Wrap</span><span class="rule"></span><span class="price">$ 8.99</span></div><p class="desc">Chicken cutlet with shredded lettuce, tomato, red onion, and ranch dressing.</p></li>
    <li class="item"><div class="row"><span class="name">Greek Salad Wrap</span><span class="rule"></span><span class="price">$ 8.29</span></div><p class="desc">Chopped romaine lettuce, tomatoes, cucumbers, red onions, hard<br>boiled egg, and feta cheese with house dressing.</p></li>
  </ul>

  <div class="heading" style="left:332px;width:590px;top:1387px">
    <div class="title t-xl">PANINIS</div>
    <div class="sub">SERVED WITH COMPLEMENTARY HOME MADE POTATO CHIPS</div>
  </div>
  <ul class="menu-list col-left" style="top:1513px">
    <li class="item"><div class="row"><span class="name">Blackened Chicken Panini</span><span class="rule"></span><span class="price">$ 8.99</span></div><p class="desc">Blackened chicken, cheddar cheese, grilled tomatoes, and Cajun<br>mayo - pressed to perfection.</p></li>
    <li class="item"><div class="row"><span class="name">Brooklyn Panini</span><span class="rule" style="margin-left:26px"></span><span class="price">$ 8.99</span></div><p class="desc">Italian-seasoned grilled chicken, fresh mozzarella, roasted red peppers, and balsamic vinaigrette - pressed to perfection.</p></li>
    <li class="item"><div class="row"><span class="name">Cheese Lovers Panini <span class="tag"><svg width="30" height="16" viewBox="0 0 30 16"><path d="M15 15 C8 12 6 6 8 2 C12 4 15 9 15 15Z M15 15 C22 12 25 6 23 2 C18 4 15 9 15 15Z" fill="#4f8a2b"/></svg>(veggie)</span></span><span class="rule"></span><span class="price">$ 8.49</span></div><p class="desc">Cheddar, provolone, mozzarella with grilled tomato and pesto<br>spread - pressed to perfection.</p></li>
  </ul>

  <div class="heading" style="left:1010px;width:590px;top:94px">
    <div class="title t-xl">PANINIS</div>
    <div class="sub">SERVED WITH COMPLEMENTARY HOME MADE POTATO CHIPS</div>
  </div>
  <ul class="menu-list col-right" style="top:205px">
    <li class="item"><div class="row"><span class="name">Cuban Panini</span><span class="rule" style="margin-left:26px"></span><span class="price">$ 8.99</span></div><p class="desc">Sliced roast pork and ham, Swiss cheese, pickles, and yellow<br>mustard - pressed to perfection.</p></li>
    <li class="item"><div class="row"><span class="name">Rabe Panini <span class="tag"><svg width="30" height="16" viewBox="0 0 30 16"><path d="M15 15 C8 12 6 6 8 2 C12 4 15 9 15 15Z M15 15 C22 12 25 6 23 2 C18 4 15 9 15 15Z" fill="#4f8a2b"/></svg>(veggie)</span></span><span class="rule"></span><span class="price">$ 8.99</span></div><p class="desc">Broccoli rabe, fresh mozzarella, tomato, and Kalamata olive<br>pesto - pressed to perfection.</p></li>
    <li class="item"><div class="row"><span class="name">MRD</span><span class="rule" style="margin-left:16px"></span><span class="price">$ 8.99</span></div><p class="desc">Grilled chicken, prosciutto, fresh mozzarella, pesto spread, romaine,<br>and balsamic glaze on a brick oven roll.</p></li>
  </ul>

  <div class="heading" style="left:1010px;width:590px;top:602px">
    <div class="title t-l">STEAK SANDWICHES</div>
    <div class="sub">SERVED WITH COMPLEMENTARY FRENCH FRIES</div>
  </div>
  <ul class="menu-list col-right" style="top:730px">
    <li class="item" style="--h:85px"><div class="row"><span class="name">Cheese Steak</span><span class="rule"></span><span class="price">$ 8.99</span></div><p class="desc">Topped with lettuce, tomato, and onion.</p></li>
    <li class="item" style="--h:84px"><div class="row"><span class="name">Buffalo Chicken Cheese Steak <span class="tag"><svg width="30" height="16" viewBox="0 0 30 16"><path d="M3 13 C10 13 20 9 24 3 L27 5 C22 12 12 16 3 13Z" fill="#c8201e"/><path d="M24 3 L26 0" stroke="#3b7a2a" stroke-width="2"/></svg>spicy</span></span><span class="rule" style="margin-left:26px"></span><span class="price">$ 8.99</span></div><p class="desc">Topped with buffalo sauce and bleu cheese dressing.</p></li>
    <li class="item" style="--h:84px"><div class="row"><span class="name">Broccoli Chicken Cheese Steak</span><span class="rule"></span><span class="price">$ 8.99</span></div><p class="desc">Topped with broccoli, Romano cheese, and Colby cheese on a garlic roll.</p></li>
    <li class="item" style="--h:85px"><div class="row"><span class="name">Philadelphia Cheese Steak</span><span class="rule"></span><span class="price">$ 9.49</span></div><p class="desc">Topped with sautéed peppers, onions, mushrooms, and cheese.</p></li>
    <li class="item" style="--h:84px"><div class="row"><span class="name">Triple Cheese Steak Deluxe</span><span class="rule"></span><span class="price">$ 9.49</span></div><p class="desc" style="line-height:18px;margin-top:-4px">Topped with Swiss, provolone, and American cheeses, lettuce,<br>tomato, and onion.</p></li>
  </ul>

  <div class="heading" style="left:1010px;width:590px;top:1230px">
    <div class="title t-m">CHARBROILED HAMBURGERS</div>
    <div class="sub" style="margin-top:16px">FRESH 8OZ. BURGERS SERVED SLAW &amp;<br>COMPLEMENTARY FRENCH FRIES</div>
  </div>
  <ul class="menu-list col-right" style="top:1394px">
    <li class="item" style="--h:84px"><div class="row"><span class="name">Cheeseburger Deluxe</span><span class="rule" style="margin-left:26px"></span><span class="price">$ 8.49</span></div><p class="desc">With romaine lettuce, tomato, and red onion on a toasted roll.</p></li>
    <li class="item" style="--h:84px"><div class="row"><span class="name">Bacon Cheeseburger Deluxe</span><span class="rule" style="margin-left:16px"></span><span class="price">$ 8.99</span></div><p class="desc">With romaine lettuce, tomato, and red onion on a toasted roll.</p></li>
    <li class="item" style="--h:85px"><div class="row"><span class="name">Chipotle Burger <span class="tag"><svg width="30" height="16" viewBox="0 0 30 16"><path d="M3 13 C10 13 20 9 24 3 L27 5 C22 12 12 16 3 13Z" fill="#c8201e"/><path d="M24 3 L26 0" stroke="#3b7a2a" stroke-width="2"/></svg>spicy</span></span><span class="rule"></span><span class="price">$ 8.99</span></div><p class="desc">Topped with pepper jack, frizzled onions, and chipotle mayo on a toasted roll.</p></li>
    <li class="item" style="--h:84px"><div class="row"><span class="name">Rodeo Burger</span><span class="rule"></span><span class="price">$ 9.49</span></div><p class="desc" style="line-height:18px;margin-top:-4px">Topped with fried onion rings, bacon, BBQ sauce, and melted Monterey Jack<br>cheese on a toasted roll.</p></li>
    <li class="item" style="--h:84px"><div class="row"><span class="name">'Shroom &amp; Swiss Burger</span><span class="rule" style="margin-left:60px"></span><span class="price">$ 8.99</span></div><p class="desc">Topped with mushrooms and melted Swiss on a toasted roll.</p></li>
  </ul>

  <div class="footer">ORDER ONLINE @MILLRUNDELI.COM</div>
</div>
</body>
</html>
```